Meridale Systems Business Card

I am a managed service provider and general business technology partner for all IT services. I really enjoy design layout of https://www.artvorlo.com/design/48206197 and would like something like this but focus graphically a little more on the constellation kind of images. I have provided my logo I want to use I own the rights to it. On the front I would like the tag line to be "Simple Solutions for Complex Connections" With the logo and attached background. The information side in the bottom left I would like "We Make IT Happen." the Logo how they did it twice I think looks great. Meridale Systems LLC for the Business name. My Name is Gareth Pellow M.S. Owner
Email: Gareth@Meridale-Sys.com
Phone:
Cell: 555-214-3096

I look forward to seeing your work

Font styles to use
Serif

```html
<!DOCTYPE html>
<html lang="en">
<head>
<meta charset="utf-8">
<title>Meridale Systems Business Card</title>
<link rel="stylesheet" href="https://fonts.googleapis.com/css2?family=Montserrat:wght@400;500;600;700;800&display=swap">
<style>
  :root {
    --backdrop: #1f1f21;
    --navy-deep: #0d1140;
    --navy: #1b2470;
    --blue: #0d5aa7;
    --blue-bright: #1f7fd0;
    --orange: #e4951f;
    --orange-deep: #e06a1c;
    --paper: #f3f3f3;
    --ink: #2a2a2a;
    --white: #ffffff;
  }
  * { box-sizing: border-box; margin: 0; padding: 0; }
  html, body { width: 1200px; height: 1021px; overflow: hidden; }
  body {
    background: var(--backdrop);
    font-family: "Montserrat", sans-serif;
    position: relative;
  }
  .card {
    position: absolute;
    left: 250px;
    width: 700px;
    height: 400px;
    overflow: hidden;
    box-shadow: 0 14px 30px rgba(0,0,0,.55);
  }

  /* Front */
  .card-front { top: 70px; }
  .front-backdrop {
    position: absolute; inset: 0;
    background: radial-gradient(ellipse at 40% 30%, var(--navy) 0%, var(--navy-deep) 75%);
  }
  .front-brand {
    position: absolute; left: 0; right: 0; top: 140px;
    display: flex; align-items: center; justify-content: center; gap: 18px;
  }
  .brand-dot {
    width: 26px; height: 26px; border-radius: 50%;
    background: var(--orange);
  }
  .front-brand .brand-name {
    font-weight: 800; font-size: 44px; letter-spacing: 1px;
    color: var(--blue-bright); text-transform: uppercase;
  }
  .front-tagline {
    position: absolute; left: 0; right: 0; bottom: 70px;
    display: flex; align-items: center; gap: 14px;
    font-weight: 600; font-size: 17px; letter-spacing: 3px;
    text-transform: uppercase; color: var(--white);
  }
  .front-tagline .rule { flex: 1; height: 2px; background: var(--orange); }
  .front-tagline .accent { color: var(--orange); }

  /* Back */
  .card-back { top: 540px; background: var(--paper); }
  .back-brand {
    position: absolute; left: 46px; top: 38px;
    display: flex; align-items: center; gap: 12px;
  }
  .back-brand .brand-dot { width: 18px; height: 18px; }
  .back-brand .brand-name {
    font-weight: 800; font-size: 27px; letter-spacing: .5px;
    color: var(--blue); text-transform: uppercase;
  }
  .name-tab {
    position: absolute; left: 0; top: 122px;
    width: 40px; height: 54px; background: var(--blue);
  }
  .person {
    position: absolute; left: 62px; top: 120px;
  }
  .person-name { font-weight: 700; font-size: 28px; color: var(--blue); }
  .person-role { font-weight: 400; font-size: 18px; color: var(--ink); letter-spacing: .5px; }
  .connector {
    position: absolute; left: 58px; top: 185px; width: 600px; height: 40px;
  }
  .contact {
    position: absolute; left: 58px; top: 215px;
    list-style: none; font-size: 19px; color: var(--ink); line-height: 28px;
  }
  .contact li { display: flex; align-items: center; gap: 10px; }
  .contact svg { width: 16px; height: 16px; flex: none; }
  .band-slogan {
    position: absolute; left: 0; bottom: 40px;
    width: 380px; height: 48px; background: var(--blue);
    clip-path: polygon(0 0, 96% 0, 100% 100%, 0 100%);
    display: flex; align-items: center; padding-left: 40px;
    font-weight: 800; font-size: 21px; color: var(--white); letter-spacing: .5px;
  }
  .band-slogan .accent { color: var(--orange); }
  .band-web {
    position: absolute; left: 392px; right: 0; bottom: 0; height: 30px;
    background: var(--orange);
    clip-path: polygon(0 0, 100% 0, 100% 100%, 2% 100%);
  }
  .band-web-base {
    position: absolute; left: 0; right: 0; bottom: 0; height: 40px; background: var(--blue);
    width: 392px;
  }
  .website {
    position: absolute; left: 420px; bottom: 48px;
    display: flex; align-items: center; gap: 10px;
    font-size: 20px; color: var(--ink);
  }
  .website svg { width: 20px; height: 20px; }
</style>
</head>
<body>

<section class="card card-front">
  <div class="front-backdrop" role="img" aria-label="Deep navy background with a faint network of connected star points"></div>
  <div class="front-brand">
    <span class="brand-dot"></span>
    <span class="brand-name">Meridale Systems LLC</span>
  </div>
  <p class="front-tagline">
    <span class="rule"></span>
    <span><span class="accent">Simple Solutions</span> for Complex Connections</span>
    <span class="rule"></span>
  </p>
</section>

<section class="card card-back">
  <div class="back-brand">
    <span class="brand-dot"></span>
    <span class="brand-name">Meridale Systems LLC</span>
  </div>

  <div class="name-tab"></div>
  <div class="person">
    <p class="person-name">Gareth Pellow M.S.</p>
    <p class="person-role">OWNER</p>
  </div>

  <svg class="connector" viewBox="0 0 600 40" aria-hidden="true">
    <line x1="0" y1="2" x2="590" y2="30" stroke="#111" stroke-width="2"/>
    <circle cx="590" cy="30" r="7" fill="#111"/>
  </svg>

  <ul class="contact">
    <li>
      <svg viewBox="0 0 16 16" aria-hidden="true"><rect x="1" y="3" width="14" height="10" fill="none" stroke="#e4951f" stroke-width="1.6"/><polyline points="1,3 8,9 15,3" fill="none" stroke="#e4951f" stroke-width="1.6"/></svg>
      Gareth@Meridale-Sys.com
    </li>
    <li>
      <svg viewBox="0 0 16 16" aria-hidden="true"><rect x="4" y="1" width="8" height="14" rx="1.5" fill="none" stroke="#e4951f" stroke-width="1.6"/><line x1="7" y1="12.5" x2="9" y2="12.5" stroke="#e4951f" stroke-width="1.4"/></svg>
      555-214-3096
    </li>
  </ul>

  <div class="band-web-base"></div>
  <div class="band-web"></div>
  <div class="band-slogan"><span>WE MAKE IT&nbsp;<span class="accent">HAPPEN</span></span></div>

  <p class="website">
    <svg viewBox="0 0 20 20" aria-hidden="true"><circle cx="10" cy="10" r="8.5" fill="none" stroke="#e4951f" stroke-width="1.6"/><ellipse cx="10" cy="10" rx="3.8" ry="8.5" fill="none" stroke="#e4951f" stroke-width="1.4"/><line x1="1.5" y1="10" x2="18.5" y2="10" stroke="#e4951f" stroke-width="1.4"/></svg>
    www.Meridale-Sys.com
  </p>
</section>

</body>
</html>
```